Clever & creative business card needed for a pediatric dentist.

We need a business card for a pediatric dentist that is building a brand-new pediatric dental practice. He is funny, outgoing, and sociable, and he hopes to give his business card to dentists and pediatricians so that he can give them information of where to refer infants, children, and teenagers that need high quality and attainable dental care.

The name of the dental practice is Copper Fern Pediatric Dentistry. Logo design .png / .pdf/ .jpg are provided to aid in the design.

The dentist's last name is Tolvan (which sounds like "burger", as in "hamburger” or “cheeseburger"). Since it is pediatric practice, kudos will be given to designs that implement a little joke into the design - but hopefully in a small or hidden way (such as putting something like a cheeseburger on the back of the card, or hiding it an an abstract way).

Thank you!

Please make a design that incorporates colors. It should be fun! Not too serious. It does not have to follow the color scheme of the logos.

```html
<!DOCTYPE html>
<html lang="en">
<head>
<meta charset="utf-8">
<title>Copper Fern Pediatric Dentistry — Business Card</title>
<link rel="stylesheet" href="https://fonts.googleapis.com/css2?family=Lexend:wght@400;500&family=Plus+Jakarta+Sans:ital,wght@0,500;0,800;1,500&display=swap">
<style>
  :root {
    --backdrop: #c8c8c8;
    --card-white: #ffffff;
    --ink-grey: #3a3a3a;
    --green-deep: #1f4d2b;
    --green-top: #9bd19a;
    --green-soft: #d3e8d3;
    --art-light: #e4eef4;
    --art-edge: #cfe5cf;
  }
  * { box-sizing: border-box; margin: 0; padding: 0; }
  html, body {
    width: 1100px; height: 1200px; overflow: hidden;
    background: var(--backdrop);
  }
  .canvas { position: relative; width: 1100px; height: 1200px; }
  .card {
    position: absolute; left: 140px;
    width: 820px; height: 469px;
    box-shadow: 0 4px 10px rgba(0,0,0,0.18);
    overflow: hidden;
  }
  /* front */
  .card-front {
    top: 90px; background: var(--card-white);
    display: flex; flex-direction: column; align-items: center; justify-content: center;
  }
  .brand-dot {
    width: 74px; height: 74px; border-radius: 50%;
    background: var(--green-top); margin-bottom: 26px;
  }
  .brand-name, .brand-tagline {
    font-family: "Lexend", sans-serif; font-weight: 400; color: var(--ink-grey);
  }
  .brand-name { font-size: 66px; letter-spacing: 1px; line-height: 1; }
  .brand-tagline { font-size: 22px; letter-spacing: 9px; margin-top: 14px; }

  /* back */
  .card-back {
    top: 640px;
    background: linear-gradient(160deg, var(--green-top) 0%, #bfe0bd 45%, var(--green-soft) 70%, #b6dbb4 100%);
  }
  .person { position: absolute; left: 72px; top: 106px; }
  .person-name {
    font-family: "Plus Jakarta Sans", sans-serif; font-weight: 800;
    font-size: 46px; color: var(--green-deep); letter-spacing: -1.5px; line-height: 1;
  }
  .person-role {
    font-family: "Plus Jakarta Sans", sans-serif; font-style: italic; font-weight: 500;
    font-size: 21px; color: var(--green-deep); letter-spacing: -0.5px; margin-top: 4px;
  }
  .contact {
    position: absolute; left: 72px; top: 300px; list-style: none;
    font-family: "Plus Jakarta Sans", sans-serif; font-weight: 500;
    font-size: 21px; color: var(--green-deep); letter-spacing: -0.5px;
  }
  .contact li { display: flex; align-items: center; gap: 18px; height: 31px; }
  .contact svg { width: 17px; height: 17px; fill: var(--green-deep); }
  .mascot-art {
    position: absolute; left: 433px; top: 115px; width: 387px; height: 310px;
    border-radius: 28px 0 0 28px;
    background: linear-gradient(120deg, var(--art-edge) 0%, var(--art-light) 55%, #dbe8f2 100%);
  }
</style>
</head>
<body>
<main class="canvas">
  <section class="card card-front" aria-label="Card front">
    <div class="brand-dot"></div>
    <p class="brand-name">copper fern</p>
    <p class="brand-tagline">PEDIATRIC DENTISTRY</p>
  </section>

  <section class="card card-back" aria-label="Card back">
    <div class="person">
      <h1 class="person-name">TOLVAN</h1>
      <p class="person-role">Pediatric Dentist</p>
    </div>
    <ul class="contact">
      <li>
        <svg viewBox="0 0 24 24" aria-hidden="true"><path d="M6.6 10.8a15.5 15.5 0 0 0 6.6 6.6l2.2-2.2c.3-.3.7-.4 1-.2 1.1.4 2.3.6 3.6.6.6 0 1 .4 1 1V20c0 .6-.4 1-1 1A17 17 0 0 1 3 4c0-.6.4-1 1-1h3.5c.6 0 1 .4 1 1 0 1.3.2 2.5.6 3.6.1.3 0 .7-.2 1l-2.3 2.2z"/></svg>
        <span>+1 555 014 2270</span>
      </li>
      <li>
        <svg viewBox="0 0 24 24" aria-hidden="true"><path d="M12 2a10 10 0 1 0 0 20 10 10 0 0 0 0-20zm-1 17.9A8 8 0 0 1 4.1 10l4.9 4.9v1a2 2 0 0 0 2 2v2zm6.9-2.5A2 2 0 0 0 16 16h-1v-3a1 1 0 0 0-1-1H8v-2h2a1 1 0 0 0 1-1V7h2a2 2 0 0 0 2-2v-.4a8 8 0 0 1 2.9 12.8z"/></svg>
        <span>www.copperfernkids.com</span>
      </li>
    </ul>
    <div class="mascot-art" role="img" aria-label="Illustration of a smiling cartoon tooth character holding up a cheeseburger"></div>
  </section>
</main>
</body>
</html>
```